Beachfront Resort Landing Page

I need a design for a landing page related to a Playa Verdera Resort. This will be used as a Social Media landing page, so conversion is a must. Prefer someone with experience designing single-landing pages for conversions.

Can use this site as a reference for content / info - ramasolvento.com

The landing page needs to contain these items

"Book a 4 night Stay During the Costa Rican Green-Season, and get your 5th night Free at this All Inclusive Luxury Beachfront Resort!"

"As a Bonus, we'll throw in any of these Activities or Tours for Free! Don't wait! These will fill up fast."
"Free Massage"
"Night Hike"
"Birdwatching Tour"
"Max 2 per booking, can mix-match. While supplies last. Must redeemed during this stay" (in small print under text / images)

Also highlight these items too please

"Accessible only via boat, this Costa Rican Luxury Paradise is perfect for those wanting to escape the crowds, enjoy amazing cuisine, while swimming in our beachfront pool, and more"

"Green Season is known for whale migrations, enjoy watching the marine life from our beachfront location, or up close and personal via kayak or paddleboard"

"Paddleboards, kayaks, snorkeling gear, and more are free during your stay."

"Enjoy fresh cuisine and unique beverages daily"

"Nubeway Internet Access Included with all Bookings"

The landing page must have
- A contact form close to above the fold area
- Booking dates function around the same area
- CTA's related to most of whats mentioned above
- Can use images from the real site - ramasolvento.com
- Areas for videos on the landing page
- Must resemble a good landing page design for conversion, not a standard web-page. Those who know, will know.

Please let me know if you have any questions.

```html
<!DOCTYPE html>
<html lang="en">
<head>
<meta charset="utf-8">
<title>Playa Verdera Resort – Green Season Offer</title>
<link href="https://fonts.googleapis.com/css2?family=Oswald:wght@400;500;600&family=Montserrat:ital,wght@0,400;0,500;0,600;1,400&display=swap" rel="stylesheet">
<style>
:root{
  --green:#3f6b4a;
  --green-dark:#2f5238;
  --ink:#2c332e;
  --text:#3a3f3b;
  --muted:#7b817c;
  --olive:#8b7f2e;
  --line:#d9dcd9;
  --white:#ffffff;
}
*{margin:0;padding:0;box-sizing:border-box}
html,body{width:1200px;height:5106px;overflow:hidden}
body{position:relative;background:var(--white);font-family:"Montserrat",sans-serif;color:var(--text)}
.abs{position:absolute}
.h-title{font-family:"Oswald",sans-serif;font-weight:600;color:var(--ink);text-transform:uppercase;letter-spacing:.2px}
.h-title em{font-style:normal;color:var(--green)}
.h-center{left:0;width:1200px;text-align:center;font-size:32px}
.rule{height:3px;width:56px;background:var(--green)}
.btn{display:flex;align-items:center;justify-content:center;border:1px solid #8a918b;border-radius:4px;font-size:11px;color:var(--green);background:var(--white)}
.photo{display:block}
.block{background:var(--green)}
p.body{font-size:15px;line-height:27px;color:var(--text)}

/* top bar & header */
.topbar{left:0;top:0;width:1200px;height:36px;background:var(--green)}
.topbar span{position:absolute;top:10px;font-size:11px;color:#e8efe9;display:flex;align-items:center;gap:6px}
.header{left:0;top:36px;width:1200px;height:84px;background:var(--white)}
.brand{display:flex;align-items:center;gap:12px}
.brand-mark{width:44px;height:44px;border-radius:50%;background:var(--green)}
.brand-name{font-family:"Oswald",sans-serif;font-weight:500;font-size:17px;line-height:20px;color:var(--ink)}

/* hero */
.hero{left:0;top:120px;width:1200px;height:565px;background:linear-gradient(180deg,#3f6446 0%,#5c7f63 14%,#8cb3bf 32%,#a9cbd6 60%,#c9dfe6 100%)}
.hero-title{left:142px;top:272px;font-family:"Oswald",sans-serif;font-weight:500;font-size:60px;line-height:68px;color:var(--white);text-transform:uppercase}
.hero-vertical{left:1120px;top:150px;width:80px;height:490px;writing-mode:vertical-rl;transform:rotate(180deg);font-family:"Oswald",sans-serif;font-weight:600;font-size:84px;line-height:80px;color:rgba(255,255,255,.9);text-transform:uppercase;white-space:nowrap;overflow:hidden}

/* booking */
.booking{left:139px;top:595px;width:919px;height:149px;background:var(--white);border-radius:8px;box-shadow:0 6px 22px rgba(0,0,0,.12)}
.booking h2{position:absolute;left:0;top:14px;width:100%;text-align:center;font-family:"Oswald",sans-serif;font-weight:500;font-size:30px;color:var(--green)}
.field{position:absolute;top:71px;height:42px;border:1px solid var(--line);border-radius:4px;font-size:11px;color:#555;padding:0 14px;display:flex;align-items:center;justify-content:space-between}
.search{position:absolute;top:71px;left:791px;width:100px;height:42px;background:var(--green);color:#fff;border-radius:4px;font-size:11px;display:flex;align-items:center;justify-content:center}

/* sections */
.bonus-label{position:absolute;left:0;bottom:22px;width:100%;padding-left:42px;font-family:"Oswald",sans-serif;font-weight:500;font-size:31px;color:#fff;text-transform:uppercase}
.feature{position:absolute;left:615px;display:flex;gap:18px;align-items:center}
.feature .icon{width:46px;height:46px;border-radius:8px;background:var(--green);display:flex;align-items:center;justify-content:center}
.feature p{font-size:12px;line-height:20px;color:var(--text);width:300px}

.quote{left:174px;top:3652px;width:430px;font-style:italic;font-size:15px;line-height:32px;color:var(--text)}
.arrow{position:absolute;top:3972px;width:32px;height:32px;border-radius:50%;display:flex;align-items:center;justify-content:center}

.newsletter-bg{left:0;top:4511px;width:1200px;height:407px;background:linear-gradient(180deg,#e3c7a8 0%,#d9b08a 30%,#c9b8a6 55%,#e2ddd3 80%,#f4f2ee 100%)}
.footer-item{position:absolute;top:4986px;display:flex;gap:12px;font-size:11px;line-height:22px;color:var(--text)}
.social{position:absolute;top:5066px;width:26px;height:26px;border-radius:50%;background:var(--green)}
.palm{background:radial-gradient(ellipse at center,rgba(222,226,214,.55) 0%,rgba(222,226,214,0) 70%)}
</style>
</head>
<body>

<!-- top bar -->
<div class="abs topbar">
  <span style="left:766px">
    <svg width="14" height="10" viewBox="0 0 14 10"><rect x=".5" y=".5" width="13" height="9" fill="none" stroke="#e8efe9"/><path d="M.5 .5 7 5.5 13.5 .5" fill="none" stroke="#e8efe9"/></svg>
    hola@playaverdera.com
  </span>
  <span style="left:958px;font-size:12px">
    <svg width="12" height="12" viewBox="0 0 24 24"><path d="M6.6 10.8a15 15 0 0 0 6.6 6.6l2.2-2.2a1 1 0 0 1 1-.25 11.4 11.4 0 0 0 3.6.6 1 1 0 0 1 1 1V20a1 1 0 0 1-1 1A17 17 0 0 1 3 4a1 1 0 0 1 1-1h3.5a1 1 0 0 1 1 1c0 1.25.2 2.45.6 3.6a1 1 0 0 1-.25 1z" fill="none" stroke="#e8efe9" stroke-width="2"/></svg>
    555 010 2040
  </span>
</div>

<!-- header -->
<header class="abs header">
  <div class="abs brand" style="left:142px;top:20px">
    <div class="brand-mark"></div>
    <div class="brand-name">Playa Verdera<br>Resort</div>
  </div>
  <div class="abs btn" style="left:972px;top:24px;width:86px;height:34px;color:#555">Login</div>
</header>

<!-- hero -->
<section class="abs hero" role="img" aria-label="Couple paddling a red kayak on turquoise water along a jungle coastline"></section>
<h1 class="abs hero-title">Luxury<br>Beachfront<br>Resort!</h1>
<div class="abs btn" style="left:142px;top:500px;width:106px;height:35px;border-color:#fff">Book Now</div>
<div class="abs hero-vertical">Verdera Resort</div>

<!-- booking form -->
<form class="abs booking">
  <h2>Book Now!</h2>
  <div class="field" style="left:30px;width:198px">Arrival
    <svg width="14" height="14" viewBox="0 0 14 14"><rect x="1" y="2" width="12" height="11" fill="none" stroke="#888"/><path d="M1 5h12M4 1v3M10 1v3" stroke="#888"/></svg></div>
  <div class="field" style="left:242px;width:196px">Departure
    <svg width="14" height="14" viewBox="0 0 14 14"><rect x="1" y="2" width="12" height="11" fill="none" stroke="#888"/><path d="M1 5h12M4 1v3M10 1v3" stroke="#888"/></svg></div>
  <div class="field" style="left:452px;width:99px">Units</div>
  <div class="field" style="left:565px;width:99px">Adults</div>
  <div class="field" style="left:678px;width:99px">Children</div>
  <div class="search">Search</div>
</form>

<!-- offer -->
<div class="abs palm" style="left:880px;top:1000px;width:320px;height:360px" role="img" aria-label="Faint palm tree decoration"></div>
<div class="abs block" style="left:125px;top:850px;width:252px;height:300px"></div>
<div class="abs photo" style="left:143px;top:829px;width:426px;height:305px;background:linear-gradient(160deg,#4d6a3a,#8a8a5a 55%,#b9a98a)" role="img" aria-label="Couple walking hand in hand along a jungle beach at sunrise"></div>
<h2 class="abs h-title" style="left:601px;top:870px;font-size:33px;line-height:40px">Book <em>4</em> Night Get<br><em>5th</em> Night Free</h2>
<p class="abs body" style="left:601px;top:964px;width:430px">Book a 4 night Stay During the Costa Rican Green-Season, and get your 5th night Free at this All Inclusive Luxury Beachfront Resort!</p>
<div class="abs btn" style="left:601px;top:1077px;width:99px;height:36px">Book Now</div>

<!-- bonus -->
<h2 class="abs h-title h-center" style="top:1222px">Get <em>Bonus</em></h2>
<div class="abs rule" style="left:572px;top:1266px"></div>
<p class="abs" style="left:0;top:1290px;width:1200px;text-align:center;font-size:15px;line-height:27px">As a <b>Bonus</b>, we'll throw in any of these <b>Activities or<br>Tours for Free!</b> Don't wait! These will fill up fast.</p>

<div class="abs block" style="left:825px;top:1370px;width:254px;height:160px"></div>
<div class="abs photo" style="left:143px;top:1390px;width:448px;height:432px;background:linear-gradient(180deg,#6f7d7a,#3d4a3f 60%,#2a2f28)" role="img" aria-label="Hiker with backpack near a jungle waterfall at dusk">
  <div class="bonus-label">Night Hike</div></div>
<div class="abs photo" style="left:609px;top:1390px;width:448px;height:208px;background:linear-gradient(135deg,#8a7b6e,#d8b8a0 55%,#f2ece6)" role="img" aria-label="Guest relaxing during a massage">
  <div class="bonus-label" style="top:36px;bottom:auto;padding-left:0;text-align:right;padding-right:56px">Free Massage</div></div>
<div class="abs photo" style="left:609px;top:1616px;width:448px;height:208px;background:linear-gradient(135deg,#1f3a1e,#3d6a2e 60%,#2a4a22)" role="img" aria-label="Toucan perched in the rainforest">
  <div class="bonus-label" style="padding-left:28px">Birdwatching Tour</div></div>
<p class="abs" style="left:0;top:1838px;width:1200px;text-align:center;font-size:10px;color:var(--muted)">*Max 2 per booking, can mix-match. While supplies last. Must redeemed during this stay</p>
<div class="abs btn" style="left:550px;top:1872px;width:100px;height:36px">Book Now</div>

<!-- boat -->
<div class="abs palm" style="left:0;top:2120px;width:300px;height:400px" role="img" aria-label="Faint palm tree decoration"></div>
<h2 class="abs h-title" style="left:143px;top:2034px;font-size:31px">Accessible <em>via Boat</em></h2>
<div class="abs rule" style="left:143px;top:2084px"></div>
<p class="abs body" style="left:143px;top:2102px;width:420px">Accessible only via boat, this Costa Rican Luxury Paradise is perfect for those wanting to escape the crowds, enjoy amazing cuisine, while swimming in our beachfront pool, and more</p>
<div class="abs btn" style="left:141px;top:2235px;width:100px;height:35px">Book Now</div>
<div class="abs block" style="left:853px;top:2122px;width:206px;height:180px"></div>
<div class="abs photo" style="left:615px;top:1979px;width:425px;height:308px;background:linear-gradient(180deg,#8d8fb0,#e3a788 35%,#5f8fb4 60%,#2d5f86)" role="img" aria-label="Passengers on a small boat crossing the bay at sunset"></div>

<!-- green season -->
<div class="abs block" style="left:125px;top:2630px;width:208px;height:182px"></div>
<div class="abs photo" style="left:143px;top:2460px;width:220px;height:340px;background:linear-gradient(180deg,#6e8aa6,#a7c2d4 45%,#5d7f9a)" role="img" aria-label="Dolphin leaping beside guests on a boat"></div>
<div class="abs photo" style="left:373px;top:2415px;width:218px;height:184px;background:linear-gradient(180deg,#3e6b38,#7aa96a 55%,#4cc6e0)" role="img" aria-label="Guests carrying a turquoise paddleboard"></div>
<div class="abs photo" style="left:373px;top:2613px;width:218px;height:187px;background:radial-gradient(circle at 50% 50%,#d99b52,#3a3a36 45%,#f2f2f0 75%)" role="img" aria-label="Plated tuna dish with fresh vegetables"></div>
<h2 class="abs h-title" style="left:615px;top:2410px;font-size:31px">Green <em>Season</em></h2>
<div class="abs rule" style="left:615px;top:2458px"></div>
<p class="abs body" style="left:615px;top:2470px;width:450px;font-size:14px;line-height:27px">Green Season is known for whale migrations, enjoy watching the marine life from our beachfront location, or up close and personal via kayak or paddleboard</p>
<div class="feature" style="top:2564px">
  <div class="icon"><svg width="24" height="24" viewBox="0 0 24 24"><path d="M6 20 18 4M8 6c3 0 6 3 6 6" fill="none" stroke="#fff" stroke-width="1.6"/><ellipse cx="8" cy="16" rx="2.5" ry="5" transform="rotate(35 8 16)" fill="none" stroke="#fff" stroke-width="1.6"/></svg></div>
  <p>Paddleboards, kayaks, snorkeling gear, and more are free during your stay.</p></div>
<div class="feature" style="top:2626px">
  <div class="icon"><svg width="24" height="24" viewBox="0 0 24 24"><circle cx="12" cy="12" r="9" fill="none" stroke="#fff" stroke-width="1.6"/><path d="M9 7v10M7 7v3a2 2 0 0 0 4 0V7M15 7v10M15 7c2 0 2 4 0 4" fill="none" stroke="#fff" stroke-width="1.4"/></svg></div>
  <p>Enjoy fresh cuisine and unique beverages daily</p></div>
<div class="feature" style="top:2688px">
  <div class="icon"><svg width="24" height="24" viewBox="0 0 24 24"><circle cx="12" cy="12" r="9" fill="none" stroke="#fff" stroke-width="1.6"/><path d="M3 12h18M12 3c3 3 3 15 0 18M12 3c-3 3-3 15 0 18" fill="none" stroke="#fff" stroke-width="1.4"/></svg></div>
  <p>Nubeway Internet Access Included with all Bookings</p></div>
<div class="abs btn" style="left:614px;top:2766px;width:100px;height:35px">Book Now</div>

<!-- gallery -->
<h2 class="abs h-title h-center" style="top:2888px">Our <em>Gallery</em></h2>
<div class="abs rule" style="left:572px;top:2936px"></div>
<div class="abs palm" style="left:1050px;top:3000px;width:150px;height:400px" role="img" aria-label="Faint palm tree decoration"></div>
<div class="abs photo" style="left:143px;top:2974px;width:295px;height:410px;background:linear-gradient(180deg,#8fb8d8,#4c7a3a 28%,#3f7a4a 48%,#3fa6b8 70%,#2e8fa8)" role="img" aria-label="Video: aerial view of the jungle coastline and beach"></div>
<svg class="abs" style="left:262px;top:3150px" width="56" height="56" viewBox="0 0 56 56"><circle cx="28" cy="28" r="28" fill="rgba(255,255,255,.55)"/><path d="M23 18v20l15-10z" fill="#fff"/></svg>
<div class="abs photo" style="left:450px;top:2974px;width:298px;height:198px;background:linear-gradient(180deg,#3f6a3a,#7fa070 45%,#7cc4cf 70%,#c8c4b8)" role="img" aria-label="Infinity pool with loungers under the trees"></div>
<div class="abs photo" style="left:450px;top:3186px;width:298px;height:198px;background:linear-gradient(180deg,#a9b86a,#c9c27a 40%,#8a6a3a)" role="img" aria-label="Pineapples and fresh fruit on the bar"></div>
<div class="abs photo" style="left:761px;top:2974px;width:298px;height:410px;background:linear-gradient(180deg,#3e6a34,#6d9a5c 35%,#5aa0c8 55%,#d9d4cc 80%)" role="img" aria-label="Set dinner table overlooking the ocean"></div>

<!-- testimonials -->
<h2 class="abs h-title h-center" style="top:3500px">What <em style="color:var(--olive)">People</em> Say</h2>
<div class="abs rule" style="left:572px;top:3548px"></div>
<div class="abs palm" style="left:0;top:3950px;width:220px;height:380px" role="img" aria-label="Faint palm tree decoration"></div>
<div class="abs block" style="left:121px;top:3599px;width:302px;height:476px"></div>
<div class="abs" style="left:139px;top:3618px;width:916px;height:437px;background:#fff;box-shadow:0 4px 22px rgba(0,0,0,.08)"></div>
<p class="abs quote">"Lorem ipsum dolor sit amet, consectetuer adipiscing elit, sed diam nonummy nibh euismod tincidunt ut laoreet dolore magna aliquam erat volutpat. Ut wisi enim ad minim veniam, quis nostrud exerci tation ullamcorper suscipit lobortis nisl ut aliquip ex ea com modo consequat. Duis autem vel eum iriure dolor in vel illum dolore eu feugiat nulla facilisis .</p>
<p class="abs" style="left:180px;top:3910px;font-size:15px;font-weight:600;color:var(--green)">Lorem ipsum dolor</p>
<p class="abs" style="left:180px;top:3934px;font-size:10px;color:var(--muted)">Sed Diam Nonummy</p>
<div class="arrow" style="left:176px;background:var(--green)"><svg width="10" height="10" viewBox="0 0 10 10"><path d="M7 1 3 5l4 4z" fill="#fff"/></svg></div>
<div class="arrow" style="left:218px;border:1px solid var(--line)"><svg width="10" height="10" viewBox="0 0 10 10"><path d="M3 1l4 4-4 4z" fill="#ccc"/></svg></div>
<div class="abs block" style="left:845px;top:3660px;width:170px;height:157px"></div>
<div class="abs photo" style="left:698px;top:3682px;width:297px;height:327px;background:linear-gradient(180deg,#4a7a4a,#6fb6c4 35%,#c9a98a 65%,#e8e0d4)" role="img" aria-label="Guest relaxing on a lounger by the pool with a drink"></div>

<!-- follow -->
<h2 class="abs h-title h-center" style="top:4160px">Follow <em>Us</em></h2>
<div class="abs rule" style="left:572px;top:4208px"></div>
<div class="abs photo" style="left:0;top:4277px;width:240px;height:234px;background:linear-gradient(180deg,#9ab4cc,#d8dde2 60%,#6c7f8e)" role="img" aria-label="Guests on a fishing boat showing a catch"></div>
<div class="abs photo" style="left:240px;top:4277px;width:240px;height:234px;background:linear-gradient(180deg,#2e2e2e,#5a4a3a 60%,#3a3a32)" role="img" aria-label="Chef presenting a plated dish"></div>
<div class="abs photo" style="left:480px;top:4277px;width:240px;height:234px;background:linear-gradient(180deg,#a8c4d8,#6a9ab4 55%,#c8b89a)" role="img" aria-label="Horseback ride along the beach"></div>
<div class="abs photo" style="left:720px;top:4277px;width:240px;height:234px;background:linear-gradient(180deg,#c4d4de,#e3e6e8 45%,#b2482e 70%,#8a9aa6)" role="img" aria-label="Guests in life vests aboard a boat"></div>
<div class="abs photo" style="left:960px;top:4277px;width:240px;height:234px;background:linear-gradient(180deg,#3c6a2e,#7aa85a 55%,#2e4e26)" role="img" aria-label="Lush tropical rainforest foliage"></div>

<!-- newsletter -->
<section class="abs newsletter-bg" role="img" aria-label="Sunset over the ocean with waves on the sand"></section>
<div class="abs" style="left:186px;top:4610px;width:826px;height:172px;border:1px solid rgba(255,255,255,.8)"></div>
<div class="abs" style="left:204px;top:4600px;width:792px;height:169px;background:rgba(63,107,74,.92)"></div>
<h2 class="abs" style="left:0;top:4627px;width:1200px;text-align:center;font-family:'Oswald',sans-serif;font-weight:500;font-size:30px;color:#fff;text-transform:uppercase">Subscribe to our Newsletter</h2>
<p class="abs" style="left:0;top:4672px;width:1200px;text-align:center;font-size:11px;color:#e6ede7">Subscribe To Our Newsletter For Regular Updates</p>
<div class="abs" style="left:339px;top:4709px;width:389px;height:34px;background:#fff;font-size:9px;color:#999;padding:12px 14px">Your Email Address</div>
<div class="abs" style="left:728px;top:4709px;width:135px;height:34px;border:1px solid #fff;color:#fff;font-size:13px;display:flex;align-items:center;justify-content:center">SUBSCRIBE</div>

<!-- footer -->
<footer>
  <div class="abs brand" style="left:142px;top:4976px">
    <div class="brand-mark"></div>
    <div class="brand-name">Playa Verdera<br>Resort</div>
  </div>
  <div class="footer-item" style="left:410px">
    <svg width="16" height="18" viewBox="0 0 16 18"><path d="M8 17s6-6 6-10A6 6 0 0 0 2 7c0 4 6 10 6 10z" fill="none" stroke="var(--green)" stroke-width="1.5"/><circle cx="8" cy="7" r="2" fill="none" stroke="var(--green)" stroke-width="1.5"/></svg>
    <span>Lorem ipsum dolor sit amet,<br>consectetuer &nbsp;12590</span></div>
  <div class="footer-item" style="left:680px">
    <svg width="16" height="16" viewBox="0 0 24 24"><path d="M6.6 10.8a15 15 0 0 0 6.6 6.6l2.2-2.2a1 1 0 0 1 1-.25 11.4 11.4 0 0 0 3.6.6 1 1 0 0 1 1 1V20a1 1 0 0 1-1 1A17 17 0 0 1 3 4a1 1 0 0 1 1-1h3.5a1 1 0 0 1 1 1c0 1.25.2 2.45.6 3.6a1 1 0 0 1-.25 1z" fill="none" stroke="var(--green)" stroke-width="2"/></svg>
    <span>Call :<br>555 010 3377</span></div>
  <div class="footer-item" style="left:859px">
    <svg width="18" height="14" viewBox="0 0 18 14"><rect x="1" y="1" width="16" height="12" fill="none" stroke="var(--green)" stroke-width="1.5"/><path d="M1 1l8 6 8-6" fill="none" stroke="var(--green)" stroke-width="1.5"/></svg>
    <span>Email :<br>reservas@playaverdera.com</span></div>
  <p class="abs" style="left:142px;top:5074px;font-size:10px;color:var(--text)">© 2024 Verdera Resort. All Right Reserved.</p>
  <div class="social" style="left:960px" aria-label="Social link"></div>
  <div class="social" style="left:996px" aria-label="Social link"></div>
  <div class="social" style="left:1032px" aria-label="Social link"></div>
</footer>

</body>
</html>
```